Designing a brochures for an educational counseling service provider

We would like a 4 sided design on a 11x8.5 paper, half folded. I have including a sample design we did to give you an idea of what we envision but we welcome creativity to make beautiful looking flyers. Text for the flier is included as well as our logo.
- The most important thing is capturing our audience/market. We will be handing these flies to schools, organizations and individual clients.

www.vormtaleducationalconsultants.com

Target Market(s)

We are targeting international students wanting to study in the U.S and Canada.

Industry/Entity Type

Education

Requirements
Must have
• - Clean and clear
• - Our logo should visible and well placed.
• - Could you the pictures of students, libraries and school buildings or you could use the pictures we already have.
Nice to have
• We would like this to match business cards.

```html
<!DOCTYPE html>
<html lang="en">
<head>
<meta charset="utf-8">
<title>Vormtal International Educational Consultants – Brochure Covers</title>
<link href="https://fonts.googleapis.com/css2?family=Montserrat:wght@500;600;700&family=Open+Sans:wght@400;600&display=swap" rel="stylesheet">
<style>
  :root{
    --navy:#173a52;
    --navy-deep:#12304a;
    --orange:#f47b12;
    --paper:#f1f1f1;
    --paper-light:#f8f8f8;
    --ring:#dfe3e6;
    --text-navy:#1d2f5e;
    --white:#ffffff;
    --stage:#e6e6e6;
  }
  *{margin:0;padding:0;box-sizing:border-box}
  html,body{width:1200px;height:927px;overflow:hidden;background:var(--stage)}
  .spread{position:absolute;left:80px;top:62px;width:1040px;height:804px;box-shadow:0 10px 30px rgba(0,0,0,.18);background:var(--paper)}
  .spread-art{position:absolute;inset:0}
  .brand{position:absolute;display:flex;align-items:center;gap:8px;font-family:'Montserrat',sans-serif}
  .brand-mark{width:22px;height:22px;border-radius:50%;background:var(--orange);flex:none}
  .brand-name{font-weight:700;color:var(--navy);letter-spacing:.5px}
  .brand-tag{font-family:'Montserrat',sans-serif;font-weight:600;font-size:8px;line-height:1.15;color:var(--navy);text-transform:uppercase}
  .back-brand{left:150px;top:282px}
  .back-brand .brand-name{font-size:30px}
  .front-brand{left:660px;top:30px}
  .front-brand .brand-name{font-size:30px}
  .world-map{position:absolute;left:200px;top:340px;width:300px;height:170px;border-radius:14px;background:radial-gradient(ellipse at center,#d6d6d6 0%,#e6e6e6 70%,rgba(236,236,236,0) 100%)}
  .student-portrait{position:absolute;left:48px;top:478px;width:160px;height:160px;border-radius:50%;border:6px solid var(--orange);background:linear-gradient(135deg,#e9e2d2,#a88466 60%,#6d5a48)}
  .contact{position:absolute;left:44px;top:654px;width:420px;font-family:'Open Sans',sans-serif;color:var(--white);font-size:12.5px;line-height:1.35}
  .contact-title{font-family:'Montserrat',sans-serif;font-weight:700;color:var(--orange);font-size:19px;letter-spacing:.5px;margin-bottom:2px}
  .contact-role{font-weight:600}
  .contact-company{color:var(--orange);font-weight:600}
  .contact-line{display:flex;align-items:flex-start;gap:8px;margin-top:3px}
  .contact-line svg{flex:none;margin-top:2px}
  .students-photo{position:absolute;left:0;top:0;width:1040px;height:804px}
  .service-label{position:absolute;font-family:'Open Sans',sans-serif;font-size:7px;color:var(--text-navy);width:80px;text-align:center}
  .headline{position:absolute;left:560px;top:660px;width:440px;text-align:center;font-family:'Montserrat',sans-serif;font-weight:600;color:var(--text-navy);font-size:20px;line-height:1.3}
  .web-pill{position:absolute;left:630px;top:758px;width:370px;height:46px;border-radius:23px 23px 0 0;background:var(--orange);color:var(--white);font-family:'Montserrat',sans-serif;font-weight:600;font-size:13px;display:flex;align-items:center;justify-content:center}
</style>
</head>
<body>
<main class="spread">
  <svg class="spread-art" width="1040" height="804" viewBox="0 0 1040 804">
    <defs>
      <clipPath id="back-panel"><rect x="0" y="0" width="520" height="804"/></clipPath>
      <linearGradient id="front-paper" x1="0" y1="0" x2="1" y2="0">
        <stop offset="0" stop-color="#e4e4e4"/>
        <stop offset=".08" stop-color="#f6f6f6"/>
        <stop offset="1" stop-color="#f2f2f2"/>
      </linearGradient>
      <linearGradient id="students-tones" x1="0" y1="0" x2="1" y2="1">
        <stop offset="0" stop-color="#9fb17a"/>
        <stop offset=".25" stop-color="#e9e9e9"/>
        <stop offset=".5" stop-color="#f0652a"/>
        <stop offset=".75" stop-color="#e8c64a"/>
        <stop offset="1" stop-color="#3c3c3c"/>
      </linearGradient>
    </defs>

    <!-- back cover -->
    <g class="back-cover" clip-path="url(#back-panel)">
      <rect width="520" height="804" fill="var(--navy)"/>
      <circle cx="580" cy="250" r="500" fill="var(--white)"/>
      <circle cx="580" cy="250" r="478" fill="var(--ring)"/>
      <circle cx="580" cy="250" r="462" fill="var(--white)"/>
      <circle cx="580" cy="250" r="430" fill="var(--paper)"/>
      <path d="M455 0 C440 120 470 230 520 300" stroke="var(--navy)" stroke-width="26" fill="none"/>
    </g>

    <!-- front cover -->
    <rect class="front-cover" x="520" y="0" width="520" height="804" fill="url(#front-paper)"/>
    <path class="students-photo-area" role="img" aria-label="Photo of a smiling group of five students holding notebooks"
          d="M540 90 L1040 90 L1040 470 C960 520 880 530 770 522 C660 512 580 440 540 330 Z"
          fill="url(#students-tones)" opacity=".85"/>

    <!-- orange sweep across the spine -->
    <path d="M392 0 C370 300 560 530 770 540 C880 546 960 520 1040 478" stroke="var(--orange)" stroke-width="26" fill="none"/>

    <!-- navy service band -->
    <path d="M630 600 C790 614 940 566 1040 506" stroke="var(--navy)" stroke-width="20" fill="none"/>
    <g class="service-icons" fill="var(--white)" stroke="var(--orange)" stroke-width="3">
      <circle cx="704" cy="606" r="22"/>
      <circle cx="792" cy="596" r="22"/>
      <circle cx="878" cy="574" r="22"/>
      <circle cx="962" cy="540" r="22"/>
    </g>
    <g fill="var(--navy)">
      <!-- school building -->
      <path d="M692 600 L704 593 L716 600 Z"/>
      <rect x="694" y="602" width="3" height="10"/><rect x="702.5" y="602" width="3" height="10"/><rect x="711" y="602" width="3" height="10"/>
      <rect x="692" y="613" width="24" height="3"/>
      <!-- application document -->
      <rect x="783" y="585" width="15" height="20" rx="1" fill="none" stroke="var(--navy)" stroke-width="2"/>
      <rect x="786" y="590" width="9" height="2"/><rect x="786" y="595" width="9" height="2"/><rect x="786" y="600" width="6" height="2"/>
      <path d="M800 586 L804 586 L802 605 Z"/>
      <!-- group of students -->
      <circle cx="870" cy="569" r="4"/><circle cx="886" cy="569" r="4"/><circle cx="878" cy="566" r="5"/>
      <path d="M864 583 C864 575 876 575 876 583 Z"/><path d="M880 583 C880 575 892 575 892 583 Z"/><path d="M870 583 C870 572 886 572 886 583 Z"/>
      <!-- graduation cap -->
      <path d="M948 536 L962 530 L976 536 L962 542 Z"/>
      <path d="M954 539 L954 546 C958 550 966 550 970 546 L970 539 L962 543 Z"/>
      <rect x="974" y="536" width="1.5" height="9"/>
    </g>
  </svg>

  <!-- back cover content -->
  <div class="brand back-brand">
    <span class="brand-mark"></span>
    <span class="brand-name">Vormtal</span>
    <span class="brand-tag">International<br>Educational<br>Consultants</span>
  </div>
  <div class="world-map" role="img" aria-label="Dotted world map"></div>
  <div class="student-portrait" role="img" aria-label="Photo of two smiling students outdoors"></div>
  <section class="contact">
    <h2 class="contact-title">CONTACT US</h2>
    <p class="contact-role">Executive Director &amp; Independent<br>Educational Consultant</p>
    <p class="contact-company">Vormtal International Educational Consultants, LLC</p>
    <p class="contact-line">
      <svg width="10" height="13" viewBox="0 0 10 13"><path d="M5 0 C2 0 0 2 0 5 C0 8 5 13 5 13 C5 13 10 8 10 5 C10 2 8 0 5 0 Z" fill="var(--orange)"/><circle cx="5" cy="5" r="2" fill="var(--navy)"/></svg>
      <span>418 Meadow Ridge Rd Suite 120, Lakeview,<br>TX 75001</span>
    </p>
    <p class="contact-line">
      <svg width="11" height="12" viewBox="0 0 11 12"><path d="M2 0 L4 3 L3 5 C4 7 5 8 7 9 L9 8 L11 10 L9 12 C4 11 0 7 0 2 Z" fill="var(--orange)"/></svg>
      <span>555-210-3847</span>
    </p>
    <p class="contact-line">
      <svg width="12" height="9" viewBox="0 0 12 9"><rect width="12" height="9" rx="1" fill="var(--orange)"/><path d="M0 0 L6 5 L12 0" stroke="var(--navy)" stroke-width="1.2" fill="none"/></svg>
      <span>maren@vormtaleducationalconsultants.com</span>
    </p>
  </section>

  <!-- front cover content -->
  <div class="brand front-brand">
    <span class="brand-mark"></span>
    <span class="brand-name">Vormtal</span>
    <span class="brand-tag">International<br>Educational<br>Consultants</span>
  </div>
  <span class="service-label" style="left:664px;top:632px">Boarding Schools</span>
  <span class="service-label" style="left:752px;top:622px">College Admission</span>
  <span class="service-label" style="left:838px;top:600px">Transfer Students</span>
  <span class="service-label" style="left:922px;top:566px">Graduate Students</span>
  <h1 class="headline">A full-service international educational consulting group serving students and families across the globe.</h1>
  <div class="web-pill">www.vormtaleducationalconsultants.com</div>
</main>
</body>
</html>
```